Project Management Book Cover Design Project

The book title is:

The Quietly Capable Task Leader

Dale Morrowfield, MSc, MBA, PMP

It is a book about professional yet common sense project management principles aimed at beginner to experienced project managers. The book is written in a conversational, informal tone with reference to best practice in project management. It is designed to be used as an accessible desk reference. I am looking for a cover design that is striking, eye catching, and professional. It can have an element of fun and informality to reflect the tone of the contents.

I have attached a copy of the draft manuscript so you can get a feel for what the book is like.

see www.tqwra.org for more about the profession of project management

Target Market(s)

Professional Project Managers of all levels (see www.tqwra.org for further information)

Industry/Entity Type

Management

Requirements
Must have
• Must be suitable for 6" x 9" book size

```html
<!DOCTYPE html>
<html lang="en">
<head>
<meta charset="utf-8">
<title>The Quietly Capable Task Leader — Cover</title>
<link rel="stylesheet" href="https://fonts.googleapis.com/css2?family=Oranienbaum&family=Cormorant+Garamond:ital,wght@1,500&family=Arimo:wght@400;700&display=swap">
<style>
  :root {
    --cover-yellow: #f7d117;
    --cover-glow: #fffbe6;
    --title-ink: #0d0b08;
    --frame-red: #b5475a;
    --frame-rose: #d98a7a;
    --frame-teal: #1f8a99;
    --ornament-teal: #2b93a3;
    --ornament-red: #c0392b;
    --ornament-gold: #e8a93a;
  }
  html, body {
    margin: 0;
    padding: 0;
    width: 901px;
    height: 1200px;
    overflow: hidden;
    background: var(--cover-yellow);
  }
  .cover {
    position: relative;
    width: 901px;
    height: 1200px;
    overflow: hidden;
    background: radial-gradient(ellipse 48% 40% at 50% 50%, var(--cover-glow) 0%, #fbe88a 40%, var(--cover-yellow) 100%);
  }
  .frame {
    position: absolute;
    inset: 0;
  }
  .corner-ornament {
    position: absolute;
    width: 150px;
    height: 150px;
    background: radial-gradient(circle at 30% 30%, var(--ornament-red) 0%, var(--ornament-gold) 35%, var(--ornament-teal) 75%, transparent 76%);
    opacity: 0.85;
  }
  .corner-ornament.top-left { top: 14px; left: 14px; }
  .corner-ornament.top-right { top: 14px; right: 14px; transform: scaleX(-1); }
  .corner-ornament.bottom-left { bottom: 14px; left: 14px; transform: scaleY(-1); }
  .corner-ornament.bottom-right { bottom: 14px; right: 14px; transform: scale(-1, -1); }

  .tagline {
    position: absolute;
    top: 112px;
    left: 0;
    right: 0;
    text-align: center;
    font-family: "Cormorant Garamond", serif;
    font-style: italic;
    font-weight: 500;
    font-size: 32px;
    line-height: 46px;
    letter-spacing: 1.5px;
    color: var(--title-ink);
  }
  .title-line {
    position: absolute;
    margin: 0;
    font-family: "Oranienbaum", serif;
    font-weight: 400;
    line-height: 1;
    color: var(--title-ink);
    white-space: nowrap;
    text-shadow: 2px 2px 0 rgba(0,0,0,0.12);
  }
  .title-the      { top: 272px; left: 102px; font-size: 118px; }
  .title-quietly  { top: 370px; left: 216px; font-size: 138px; }
  .title-capable  { top: 488px; left: 266px; font-size: 138px; }
  .title-task     { top: 600px; left: 152px; font-size: 250px; }
  .title-leader   { top: 832px; left: 482px; font-size: 118px; }

  .author {
    position: absolute;
    bottom: 40px;
    left: 0;
    right: 0;
    text-align: center;
    font-family: "Arimo", sans-serif;
    font-size: 26px;
    color: var(--title-ink);
  }
  .author-name { font-weight: 700; }
  .author-credentials { font-weight: 400; font-size: 22px; }
</style>
</head>
<body>
  <main class="cover">
    <svg class="frame" width="901" height="1200" viewBox="0 0 901 1200" aria-hidden="true">
      <rect x="22" y="22" width="857" height="1156" fill="none" stroke="var(--frame-red)" stroke-width="6"/>
      <rect x="31" y="31" width="839" height="1138" fill="none" stroke="var(--frame-rose)" stroke-width="3"/>
      <rect x="37" y="37" width="827" height="1126" fill="none" stroke="var(--frame-teal)" stroke-width="3"/>
    </svg>

    <div class="corner-ornament top-left" role="img" aria-label="Ornamental scrollwork corner in teal, red and gold"></div>
    <div class="corner-ornament top-right" role="img" aria-label="Ornamental scrollwork corner in teal, red and gold"></div>
    <div class="corner-ornament bottom-left" role="img" aria-label="Ornamental scrollwork corner in teal, red and gold"></div>
    <div class="corner-ornament bottom-right" role="img" aria-label="Ornamental scrollwork corner in teal, red and gold"></div>

    <p class="tagline">Make your own way to<br>project success</p>

    <h1 class="book-title">
      <span class="title-line title-the">The</span>
      <span class="title-line title-quietly">Quietly</span>
      <span class="title-line title-capable">Capable</span>
      <span class="title-line title-task">Task</span>
      <span class="title-line title-leader">Leader</span>
    </h1>

    <p class="author"><span class="author-name">Dale Morrowfield,</span> <span class="author-credentials">MSc, MBA, PMP</span></p>
  </main>
</body>
</html>
```